The Corvanta Group's website for high impact furniture promotions

I am looking for a simple website. we are a promotional company that runs events for furniture stores to increase sales for short periods of time. i would like the website to have about 4 areas to explain our company. I would like it to be simple and user friendly. I would like a link to chatterbook and a contact section. I am attaching our logo that i would like somewhere large or possibly in the backround. I am open to different color schemes. I would like to convey fast paced, modern, reliable. I am open to all different styles and look forward to seeing whats out there. we are looking for a quick turn around, so if we see one that we like quick, we will pick that one thanks
Updates
Project Deadline Extended
Reason: looking for some really creative designs and want to give a fair amount of time to produce
Target Market(s)
Retail Furniture store owners
Industry/Entity Type
It Company
Number of Pages Required
1 page
Colors
Designer to choose colors to be used in the design.
Look and feel
Each slider illustrates characteristics of the customer's brand and the style your logo design should communicate.

```html
<!DOCTYPE html>
<html lang="en">
<head>
<meta charset="utf-8">
<title>The Corvanta Group – Furniture Promotions</title>
<link href="https://fonts.googleapis.com/css2?family=Montserrat:wght@500;600;700;800&family=Lato:wght@400;700&display=swap" rel="stylesheet">
<style>
:root{
  --red:#e8474a;
  --red-dark:#d23a3d;
  --navy:#2a3142;
  --navy-deep:#222838;
  --gold:#c9a45c;
  --ink:#2b2b2b;
  --muted:#6b6b6b;
  --light:#eef0f3;
  --white:#ffffff;
}
*{margin:0;padding:0;box-sizing:border-box}
html,body{width:1200px;height:5322px;overflow:hidden}
body{font-family:"Lato",sans-serif;color:var(--ink);background:var(--white);position:relative}
h1,h2,h3,h4,.nav,.btn{font-family:"Montserrat",sans-serif}
.section{position:relative;width:1200px;overflow:hidden}
.fill{position:absolute}

/* hero */
.hero{height:700px;background:linear-gradient(180deg,#3b2a2a 0%,#6a3a36 45%,#2d2424 100%)}
.hero .fill{inset:0;background:radial-gradient(ellipse at 60% 30%,#a05a4a 0%,#5a3430 45%,#241c1c 100%)}
.brand-box{position:absolute;left:120px;top:0;width:260px;height:390px;background:var(--navy);text-align:center;padding-top:46px}
.brand-mark{width:130px;height:130px;border-radius:50%;background:var(--gold);margin:0 auto 26px}
.brand-name{font-family:"Montserrat",sans-serif;font-weight:600;color:var(--white);font-size:26px;letter-spacing:4px;line-height:1.3}
.brand-sub{font-size:11px;letter-spacing:2px;color:#c9ccd4;margin-top:10px}
.socials{display:flex;gap:18px;justify-content:center;margin-top:34px}
.socials span{font-size:13px;color:var(--white);font-weight:700}
.nav{position:absolute;right:120px;top:46px;display:flex;gap:30px;font-size:14px;font-weight:700;color:var(--white);align-items:center}
.nav .active{background:var(--red);padding:12px 18px}
.hero-title{position:absolute;left:0;right:0;top:300px;text-align:center;color:var(--white)}
.hero-title .l1{font-size:64px;font-weight:800}
.hero-title .l2{font-size:88px;font-weight:800;line-height:1}
.hero-title .l2 em{font-style:normal;color:var(--red)}
.hero-meta{display:flex;justify-content:center;gap:60px;font-family:"Montserrat",sans-serif;font-weight:700;font-size:17px;margin-top:10px}
.hero-meta span:first-child{background:var(--red);padding:4px 12px}

/* partners */
.partners{height:120px;background:var(--white);display:flex;align-items:center;justify-content:center;gap:64px;border-bottom:1px solid #eee}
.badge{height:44px;background:#d8dbe0;border-radius:4px}

/* headings */
.head{text-align:center}
.head h2{font-size:56px;font-weight:800;color:var(--ink)}
.head h2.left{text-align:left}
.rule{width:60px;height:5px;background:var(--red);margin:14px auto 0}

/* steps */
.steps{height:500px;padding-top:70px}
.steps .kicker{text-align:center;font-family:"Montserrat",sans-serif;font-weight:600;font-size:28px}
.steps .title{text-align:center;font-family:"Montserrat",sans-serif;font-weight:800;font-size:56px;margin-top:8px}
.steps .title em{font-style:normal;color:var(--red)}
.step-row{display:flex;justify-content:space-between;width:960px;margin:48px auto 0}
.step{width:190px}
.step .ico{width:110px;height:110px;margin-left:30px}
.step h4{font-size:16px;font-weight:800;margin-top:26px}
.step p{font-size:15px;color:var(--muted);line-height:1.35;margin-top:6px}

/* gallery */
.gallery{height:660px;padding-top:50px}
.grid{position:absolute;top:140px;left:0;width:1200px;height:490px;display:grid;grid-template-columns:repeat(6,1fr);grid-template-rows:1fr 1fr;gap:4px}
.grid div{background:linear-gradient(135deg,#d8d3cb,#a89f93)}
.grid .tile-b{background:linear-gradient(135deg,#e6e2dc,#8d7d6a)}
.grid .hover{background:rgba(232,71,74,.88);grid-column:2/4;color:var(--white);font-family:"Montserrat",sans-serif;font-weight:800;font-size:24px;padding:120px 0 0 60px;line-height:1.3}

/* about */
.about{height:640px}
.about h2{position:absolute;left:170px;top:90px;font-size:56px;font-weight:800}
.about .rule{position:absolute;left:170px;top:162px;margin:0}
.about p{position:absolute;left:170px;width:420px;font-size:16px;line-height:1.6;color:var(--muted)}
.frame{position:absolute;left:720px;top:90px;width:480px;height:470px;border:10px solid var(--red);border-right:none}
.video{position:absolute;left:700px;top:120px;width:470px;height:380px;background:linear-gradient(135deg,#dfe5dd,#8fa08b)}
.play{position:absolute;left:906px;top:282px;width:60px;height:60px;border-radius:50%;background:var(--white)}

/* team */
.team{height:540px;background:var(--light)}
.team h2{position:absolute;left:170px;top:70px;font-size:56px;font-weight:800}
.team .rule{position:absolute;left:170px;top:142px;margin:0}
.arrows{position:absolute;right:170px;top:90px;display:flex;gap:6px}
.arrows span{width:34px;height:34px;background:var(--white);display:block}
.arrows span.on{background:var(--red)}
.members{position:absolute;left:170px;top:200px;display:flex;gap:64px}
.member{width:172px}
.member .photo{width:172px;height:200px;background:linear-gradient(180deg,#b8b4ae,#5b5750)}
.member .photo.sel{outline:8px solid var(--red);outline-offset:-8px}
.member h4{font-size:20px;font-weight:800;margin-top:18px}
.member h4 em{font-style:normal;color:var(--red)}
.member p{font-size:15px;color:var(--muted)}

/* newsletter */
.newsletter{height:280px;background:var(--navy);color:var(--white);text-align:center;padding-top:60px}
.newsletter h3{font-size:40px;font-weight:800}
.newsletter p{font-size:16px;margin-top:4px}
.sub-form{display:flex;width:920px;margin:36px auto 0}
.sub-form .field{flex:1;height:56px;background:var(--white);color:#999;text-align:left;padding:18px 24px;font-size:14px}
.sub-form .btn{width:220px;background:var(--red);font-weight:700;font-size:16px;padding-top:18px}

/* news */
.news{height:640px}
.news h2{position:absolute;left:170px;top:70px;font-size:56px;font-weight:800}
.news .rule{position:absolute;left:170px;top:142px;margin:0}
.posts{position:absolute;left:170px;top:200px;display:flex;gap:56px}
.post{width:290px}
.post .pic{height:160px;background:linear-gradient(135deg,#cfc6bb,#6e5a48)}
.post .pic.sel{outline:8px solid var(--red);outline-offset:-8px}
.post h4{font-size:16px;font-weight:800;margin-top:22px;line-height:1.3}
.post p{font-size:15px;color:var(--muted);margin-top:8px;line-height:1.4}
.news .more{position:absolute;left:520px;top:540px;width:160px;height:50px;background:var(--red);color:var(--white);font-size:15px;font-weight:700;text-align:center;padding-top:16px}

/* testimonials */
.testimonials{height:480px;background:var(--red);color:var(--white);text-align:center;padding-top:60px}
.testimonials h2{font-size:56px;font-weight:800;color:var(--white)}
.testimonials .rule{background:var(--white)}
.quote{width:860px;margin:40px auto 0;font-style:italic;font-size:19px;line-height:1.75}
.avatar{width:70px;height:70px;border-radius:50%;background:#f3c4c5;margin:26px auto 10px}
.testimonials h4{font-size:16px;font-weight:800}
.testimonials .role{font-size:14px}
.chev{position:absolute;top:250px;font-size:40px;font-family:"Montserrat",sans-serif}

/* footer */
.map{height:180px;background:linear-gradient(180deg,#e9e6df,#dad6cd)}
.pin{position:absolute;left:790px;top:50px;width:18px;height:18px;border-radius:50%;background:var(--red)}
.footer{height:582px;background:var(--navy-deep);color:var(--white)}
.foot-brand{position:absolute;left:140px;top:150px;text-align:center;width:240px}
.contact{position:absolute;left:420px;top:-120px;width:380px;height:640px;background:var(--white);color:var(--ink);text-align:center;padding-top:40px}
.contact h3{font-size:36px;font-weight:800}
.contact .rule{margin-top:10px}
.inp{width:280px;height:46px;border-bottom:1px solid #ccc;margin:10px auto 0;font-size:16px;color:#666;padding-top:18px}
.contact .btn{width:160px;height:50px;background:var(--red);color:var(--white);margin:56px auto 0;font-size:15px;font-weight:700;padding-top:16px}
.addr{position:absolute;left:860px;top:70px;width:260px}
.addr h4{font-size:20px;font-weight:700;letter-spacing:1px;color:var(--red)}
.addr .row{display:flex;gap:12px;margin-top:26px;font-size:15px;line-height:1.5;color:#c9ccd4}
.addr .row b{color:var(--white)}
.addr .phone{font-size:26px;color:var(--white)}
.addr .socials{justify-content:flex-start;margin-top:30px}
</style>
</head>
<body>

<header class="section hero">
  <div class="fill" role="img" aria-label="Photo of a speaker on stage addressing a conference audience"></div>
  <div class="brand-box">
    <div class="brand-mark"></div>
    <div class="brand-name">THE<br>CORVANTA<br>GROUP</div>
    <div class="brand-sub">HIGH IMPACT FURNITURE PROMOTIONS</div>
    <div class="socials"><span>chatterbook</span><span>chirper</span><span>circleup</span><span>linkwork</span></div>
  </div>
  <nav class="nav"><span>HOME</span><span>ABOUT</span><span>TRADE SHOW</span><span>SERVICES</span><span>TEAM</span><span>GALLERY</span><span>VIDEOS</span><span>NEWS</span><span class="active">CONTACT US</span></nav>
  <div class="hero-title">
    <div class="l1">Be a part of</div>
    <div class="l2"><em>Our Event</em> 2017</div>
    <div class="hero-meta"><span>17-21 OCTOBER</span><span>CITY HERE</span><span>2017 EDITION</span></div>
  </div>
</header>

<section class="section partners" aria-label="Partners">
  <div class="badge" style="width:110px"></div>
  <div class="badge" style="width:90px"></div>
  <div class="badge" style="width:80px"></div>
  <div class="badge" style="width:100px"></div>
  <div class="badge" style="width:120px"></div>
  <div class="badge" style="width:100px"></div>
  <div class="badge" style="width:70px;border-radius:22px"></div>
</section>

<section class="section steps">
  <div class="kicker">Let us put your sales worries to</div>
  <div class="title">rest in <em>4 Easy Steps</em></div>
  <div class="step-row">
    <div class="step">
      <svg class="ico" viewBox="0 0 110 110"><circle cx="55" cy="55" r="50" fill="none" stroke="#e8474a" stroke-width="3"/><rect x="38" y="38" width="34" height="32" fill="none" stroke="#e8474a" stroke-width="3"/><line x1="38" y1="47" x2="72" y2="47" stroke="#e8474a" stroke-width="3"/><circle cx="92" cy="18" r="14" fill="#e8474a"/><text x="92" y="24" font-size="16" font-weight="700" fill="#fff" text-anchor="middle" font-family="Montserrat,sans-serif">1</text></svg>
      <h4>LOREM IPSUM DOLOR</h4><p>Mauris accumsan, purus sed maximus, lorem nulla volutpat diam.</p>
    </div>
    <div class="step">
      <svg class="ico" viewBox="0 0 110 110"><circle cx="55" cy="55" r="50" fill="none" stroke="#e8474a" stroke-width="3"/><rect x="34" y="48" width="42" height="20" rx="6" fill="none" stroke="#e8474a" stroke-width="3"/><rect x="40" y="38" width="30" height="14" rx="4" fill="none" stroke="#e8474a" stroke-width="3"/><circle cx="92" cy="18" r="14" fill="#e8474a"/><text x="92" y="24" font-size="16" font-weight="700" fill="#fff" text-anchor="middle" font-family="Montserrat,sans-serif">2</text></svg>
      <h4>LOREM IPSUM DOLOR</h4><p>Mauris accumsan, purus sed maximus, lorem nulla volutpat diam.</p>
    </div>
    <div class="step">
      <svg class="ico" viewBox="0 0 110 110"><circle cx="55" cy="55" r="50" fill="none" stroke="#e8474a" stroke-width="3"/><rect x="38" y="58" width="7" height="14" fill="#e8474a"/><rect x="51" y="50" width="7" height="22" fill="#e8474a"/><rect x="64" y="42" width="7" height="30" fill="#e8474a"/><circle cx="92" cy="18" r="14" fill="#e8474a"/><text x="92" y="24" font-size="16" font-weight="700" fill="#fff" text-anchor="middle" font-family="Montserrat,sans-serif">3</text></svg>
      <h4>LOREM IPSUM DOLOR</h4><p>Mauris accumsan, purus sed maximus, lorem nulla volutpat diam.</p>
    </div>
    <div class="step">
      <svg class="ico" viewBox="0 0 110 110"><circle cx="55" cy="55" r="50" fill="none" stroke="#e8474a" stroke-width="3"/><path d="M40 70 L70 40 M60 40 L70 40 L70 50" fill="none" stroke="#e8474a" stroke-width="3"/><circle cx="92" cy="18" r="14" fill="#e8474a"/><text x="92" y="24" font-size="16" font-weight="700" fill="#fff" text-anchor="middle" font-family="Montserrat,sans-serif">4</text></svg>
      <h4>LOREM IPSUM DOLOR</h4><p>Mauris accumsan, purus sed maximus, lorem nulla volutpat diam.</p>
    </div>
  </div>
</section>

<section class="section gallery">
  <div class="head"><h2>OUR GALLERY</h2><div class="rule"></div></div>
  <div class="grid">
    <div role="img" aria-label="Photo of a bright interior with windows"></div>
    <div class="hover">PHOTO TITLE<br>APPEARS ON<br>MOUSE HOVER</div>
    <div class="tile-b" role="img" aria-label="Photo of a modern kitchen"></div>
    <div role="img" aria-label="Photo of a dining area"></div>
    <div class="tile-b" role="img" aria-label="Photo of a living room"></div>
    <div role="img" aria-label="Photo of a white hallway"></div>
    <div class="tile-b" role="img" aria-label="Photo of a staircase"></div>
    <div role="img" aria-label="Photo of a lounge interior"></div>
    <div class="tile-b" role="img" aria-label="Photo of a kitchen with wood cabinets"></div>
    <div role="img" aria-label="Photo of an open plan room"></div>
    <div class="tile-b" role="img" aria-label="Photo of a sitting room"></div>
  </div>
</section>

<section class="section about">
  <h2>ABOUT US</h2><div class="rule"></div>
  <p style="top:210px">Lorem ipsum dolor sit amet, consectetur adipiscing elit. Mauris accumsan, purus vel hendrerit maximus, lorem nulla venenatis elit, vitae volutpat diam ipsum ut ligula.</p>
  <p style="top:340px">Duis dolor urna, accumsan a augue et, feugiat sagittis elit. Mauris scelerisque orci vitae dui fermentum, nec mollis lectus volutpat. Nullam tincidunt enim lobortis ultricies gravida. Curabitur scelerisque ac tortor eget aliquet. In et ultricies ligula, non lacinia lorem.</p>
  <div class="frame"></div>
  <div class="video" role="img" aria-label="Video still of a living room with a sofa and plants"></div>
  <svg class="play" viewBox="0 0 60 60" style="background:none"><circle cx="30" cy="30" r="30" fill="#fff"/><path d="M24 18 L42 30 L24 42 Z" fill="#e8474a"/></svg>
</section>

<section class="section team">
  <h2>OUR TEAM</h2><div class="rule"></div>
  <div class="arrows"><span></span><span class="on"></span></div>
  <div class="members">
    <div class="member"><div class="photo" role="img" aria-label="Portrait of the founder"></div><h4><em>Reid</em> Calloway</h4><p>Founder &amp; CEO</p></div>
    <div class="member"><div class="photo sel" role="img" aria-label="Portrait of the co-founder"></div><h4><em>Nora</em> Pellam</h4><p>Co-Founder</p></div>
    <div class="member"><div class="photo" role="img" aria-label="Portrait of the managing director"></div><h4><em>Owen</em> Strake</h4><p>Managing Director</p></div>
    <div class="member"><div class="photo" role="img" aria-label="Portrait of the advert manager"></div><h4><em>Dale</em> Merrick</h4><p>Advert Manager</p></div>
  </div>
</section>

<section class="section newsletter">
  <h3>FREE NEWSLETTER</h3>
  <p>Lorem ipsum dolor sit amet, consectetur adipiscing elit.</p>
  <div class="sub-form"><div class="field">Email Address</div><div class="btn">SUBSCRIBE ➤</div></div>
</section>

<section class="section news">
  <h2>LATEST NEWS</h2><div class="rule"></div>
  <div class="posts">
    <div class="post"><div class="pic" role="img" aria-label="Photo of a furniture showroom"></div><h4>1 YEAR AGO, WE WERE JUST WRAPPING UP SEASON. NOW WE LIKE FRIDAY NIGHTS.</h4><p>Lorem ipsum dolor sit amet, cons adipiscing elit. Mauris accumsan, pure vel hendrerit maximus.</p></div>
    <div class="post"><div class="pic sel" role="img" aria-label="Photo of a dining table set"></div><h4>1 YEAR AGO, WE WERE JUST WRAPPING UP SEASON. NOW WE LIKE FRIDAY NIGHTS.</h4><p>Lorem ipsum dolor sit amet, cons adipiscing elit. Mauris accumsan, pure vel hendrerit maximus.</p></div>
    <div class="post"><div class="pic" role="img" aria-label="Photo of a dining room with pendant lights"></div><h4>1 YEAR AGO, WE WERE JUST WRAPPING UP SEASON. NOW WE LIKE FRIDAY NIGHTS.</h4><p>Lorem ipsum dolor sit amet, cons adipiscing elit. Mauris accumsan, pure vel hendrerit maximus.</p></div>
  </div>
  <div class="more btn">READ ALL NEWS ➤</div>
</section>

<section class="section testimonials">
  <h2>TESTIMONIALS</h2><div class="rule"></div>
  <p class="quote">“ Fusce ut mattis lacus, vel accumsan ligula. Sed cursus diam vel odio pellentes que cursus. Donec augue diam, malesuada ut fringilla convallis, mattis ut neque. Ut eget suscipit enim. Curabitur ullam metus, a tincidunt erat aliquam nec. Suspendisse risus ex, gravida et leo vel, posuere ornare est. ”</p>
  <div class="avatar" role="img" aria-label="Client portrait"></div>
  <h4>SAM TOLLIVER</h4><div class="role">Client</div>
  <span class="chev" style="left:150px">‹</span><span class="chev" style="right:150px">›</span>
</section>

<section class="section map" role="img" aria-label="Street map showing the office location">
  <div class="pin"></div>
</section>

<footer class="section footer" style="overflow:visible">
  <div class="foot-brand">
    <div class="brand-mark"></div>
    <div class="brand-name">THE<br>CORVANTA<br>GROUP</div>
    <div class="brand-sub">HIGH IMPACT FURNITURE PROMOTIONS</div>
  </div>
  <div class="contact">
    <h3>CONTACT US</h3><div class="rule"></div>
    <div class="inp">Enter Your Name</div>
    <div class="inp">Enter Your Email</div>
    <div class="inp">Enter Your Phone No.</div>
    <div class="inp">Subject</div>
    <div class="inp">Enter Your Message</div>
    <div class="btn">SUBMIT ➤</div>
  </div>
  <div class="addr">
    <h4>OUR ADDRESS</h4>
    <div class="row"><svg width="18" height="22" viewBox="0 0 18 22"><path d="M9 1a7 7 0 0 0-7 7c0 5 7 13 7 13s7-8 7-13a7 7 0 0 0-7-7z" fill="none" stroke="#e8474a" stroke-width="2"/><circle cx="9" cy="8" r="2.5" fill="#e8474a"/></svg><div><b>The Corvanta Group</b><br>418 Brindlewood Ct, Fairhaven,<br>NC 27000, United States</div></div>
    <div class="row"><svg width="22" height="22" viewBox="0 0 22 22"><path d="M5 2l4 4-2 3c1 3 3 5 6 6l3-2 4 4-3 3C9 20 2 13 2 5z" fill="none" stroke="#e8474a" stroke-width="2"/></svg><span class="phone">555 010 4172</span></div>
    <div class="row"><svg width="22" height="16" viewBox="0 0 22 16"><rect x="1" y="1" width="20" height="14" fill="none" stroke="#e8474a" stroke-width="2"/><path d="M1 1l10 8 10-8" fill="none" stroke="#e8474a" stroke-width="2"/></svg><span>hello@corvantagroup.example</span></div>
    <div class="socials"><span>chatterbook</span><span>chirper</span><span>linkwork</span></div>
  </div>
</footer>

</body>
</html>
```